Refresh of a rather different IT outfit website

Our web site is starting to show it's age. You can see the existing site here: www.plumbcorner.net. As a growing company we want to come across as a dynamic collection of IT experts.

We want to update the design so are open to any colour palette and look, but want to retain our current table logo. We use the logo on our business cards but with a white background - see the attached file, so you don't need to keep the brown or the green.

The design should consider the range of browsers that will be looking at the site - so please show how it will look on a wide screen laptop and a 768x1024 tablet.

We want to add some pages about our team and their skills, probably with photos of each person on the team.

This is an uncoded project - the PSD files of the design is required, not coding.
Updates

Thanks everyone for the submissions so far.  It's a holiday day in the UK today but we will get some feedback on the designs so far out to you.

Target Market(s)

Architects and other creative types looking for IT support

Industry/Entity Type

Business

Font styles to use
Serif
Sans Serif

Requirements
Must have
• Must look good on a laptop and an iPad.

```html
<!DOCTYPE html>
<html lang="en">
<head>
<meta charset="utf-8">
<title>plumbcorner – Serious IT support for business</title>
<link rel="stylesheet" href="https://fonts.googleapis.com/css2?family=Open+Sans:ital,wght@0,400;0,600;0,700;1,700&family=Great+Vibes&display=swap">
<style>
:root{
  --plum:#8e0a4d;
  --gold:#e0ae12;
  --ink:#333;
  --rule:#dcdcdc;
  --panel:#efefef;
  --footer:#333;
  --footer-text:#fff;
}
*{box-sizing:border-box;margin:0;padding:0}
html,body{width:1034px;height:1200px;overflow:hidden;background:#fff}
body{font-family:"Open Sans",Arial,sans-serif;color:var(--ink);position:relative}
.abs{position:absolute}
.topbar{left:0;top:0;width:1034px;height:3px;background:var(--plum)}
.brand{left:197px;top:24px;display:flex;align-items:center;gap:14px}
.brand-mark{width:34px;height:34px;background:var(--gold)}
.brand-name{font-size:42px;font-weight:600;color:var(--plum);line-height:1;letter-spacing:-.5px}
.callus{right:191px;top:17px;font-size:14px;color:#444;letter-spacing:.3px}
.social{right:191px;top:55px;display:flex;gap:8px}
.social span{width:27px;height:27px;border-radius:50%;background:#e6e6e6;box-shadow:0 1px 2px rgba(0,0,0,.25)}
.social span:first-child{background:#2a9ad6}
.nav{left:197px;top:96px;display:flex;font-size:9.5px;font-weight:600;letter-spacing:.3px;color:#444}
.nav a{color:inherit;text-decoration:none;padding:0 17px;border-left:1px solid #bbb;line-height:13px}
.nav a:first-child{border:0;padding-left:3px;color:var(--plum);position:relative}
.nav a:first-child::after{content:"";position:absolute;left:0;right:-13px;top:22px;height:3px;background:var(--plum)}
.hero{left:0;top:123px;width:1034px;height:330px;background:radial-gradient(ellipse at 50% 30%,#e8f5fd 0%,#9fd2f2 35%,#5aa8de 75%,#3f8fcb 100%)}
.hero-title{left:0;width:1034px;top:132px;text-align:center;font-family:"Great Vibes",cursive;font-size:34px;font-weight:400;color:#1d1d1d;text-shadow:0 1px 0 #fff}
.dots{left:777px;top:385px;display:flex;gap:7px}
.dots i{width:11px;height:11px;border-radius:50%;background:#fff;border:2px solid #d6e9f6}
.dots i:first-child{background:var(--plum)}
.hero-rule{left:0;top:452px;width:1034px;height:3px;background:var(--plum)}
.band{left:0;top:455px;width:1034px;height:50px;background:linear-gradient(#ececec,#fff)}
.service{top:425px;width:140px;text-align:center;font-size:10px;font-weight:600;color:#222;white-space:nowrap}
.service .disc{width:52px;height:52px;margin:0 auto 12px;border-radius:50%;background:#5a5a5a;border:3px solid #fff;box-shadow:0 2px 4px rgba(0,0,0,.35);display:flex;align-items:center;justify-content:center}
.service.active .disc{background:var(--plum);border-bottom-color:var(--gold)}
.head{font-style:italic;font-weight:700;font-size:17px;color:var(--plum);border-bottom:1px solid var(--rule);padding-bottom:3px;letter-spacing:-.3px}
.about{left:197px;top:532px;width:416px}
.about p{font-size:10.3px;line-height:18px;margin-top:12px;color:#333}
.about p+p{margin-top:13px}
.readmore{display:block;text-align:right;color:var(--gold);font-size:11px;margin-top:6px}
.team{left:642px;top:528px;width:192px;height:192px;border-radius:50%;border:3px solid var(--plum);overflow:hidden;box-shadow:0 8px 10px -6px rgba(0,0,0,.35);background:#fff}
.team-photo{position:absolute;left:0;top:0;width:100%;height:130px;background:linear-gradient(#e9eef3,#b9cbe0)}
.team-label{position:absolute;left:0;top:130px;width:100%;height:62px;background:var(--plum);color:#fff;text-align:center;font-size:21px;font-weight:600;padding-top:6px}
.col{top:755px;width:311px}
.card{margin-top:9px;height:226px;background:var(--panel);border:1px solid #ccc;box-shadow:inset 0 0 0 3px #fff,0 8px 8px -6px rgba(0,0,0,.35);padding:10px 14px}
.testi{display:flex;height:102px;border-bottom:1px solid #ddd}
.testi+.testi{border:0;padding-top:6px}
.person{width:100px;text-align:center}
.avatar{width:56px;height:56px;margin:2px auto 3px;border-radius:50%;border:3px solid #fff;box-shadow:0 1px 3px rgba(0,0,0,.3);background:linear-gradient(#dde3ea,#8c98a8)}
.person b{display:block;font-size:12px;line-height:15px;font-weight:600;color:#222}
.person small{display:block;font-size:8.5px;line-height:11px;color:#777}
.quote{position:relative;flex:1;font-size:8.5px;line-height:12.8px;color:#333;padding:10px 0 0 16px;border-left:1px solid #ddd;margin-left:6px}
.quote::before{content:"\201C";position:absolute;left:2px;top:-4px;font-size:22px;color:#888;font-family:Georgia,serif}
.news{display:flex;gap:14px;height:75px;border-bottom:1px solid #ddd;padding-top:6px}
.news:last-child{border:0}
.news time{display:block;color:var(--plum);font-size:10px;font-weight:600;margin-bottom:3px}
.news p{font-size:10px;line-height:14px;color:#333}
.pager{margin-top:6px;display:flex;justify-content:center;gap:6px}
.footer{left:0;top:1058px;width:1034px;height:120px;background:var(--footer)}
.foot{color:var(--footer-text)}
.fh{font-size:13px;color:var(--footer-text)}
.links{display:grid;grid-template-columns:85px 85px;row-gap:6px;margin-top:14px;font-size:8.5px;line-height:12px;letter-spacing:.2px;color:var(--footer-text)}
.links span::before{content:"›";color:var(--gold);margin-right:8px}
.vr{top:1100px;width:1px;height:55px;background:#555}
.news-form p{font-size:9px;line-height:11px;margin-top:10px}
.email{margin-top:6px;width:114px;height:17px;background:#fff;color:#999;font-size:8px;padding:3px 6px;border:1px solid #ccc}
.submit{margin-top:6px;display:inline-block;background:var(--plum);border:1px solid #fff;font-size:9px;font-weight:700;padding:2px 8px;color:#fff}
.map{left:635px;top:1100px;width:81px;height:62px;background:linear-gradient(135deg,#e5e2da,#c9c4b8)}
.cinfo{left:727px;top:1100px;font-size:9px;line-height:11px;color:var(--footer-text)}
.cinfo div{display:flex;gap:8px;margin-bottom:6px;align-items:flex-start}
.cinfo svg{flex:none;margin-top:1px}
.bottombar{left:0;top:1178px;width:1034px;height:22px;background:var(--plum);color:#fff;font-size:10px;text-align:center;line-height:22px}
</style>
</head>
<body>
<div class="abs topbar"></div>

<header>
  <div class="abs brand"><span class="brand-mark"></span><span class="brand-name">plumbcorner</span></div>
  <div class="abs callus">CALL US: 020 7946 0123</div>
  <div class="abs social" aria-label="Social links"><span></span><span></span><span></span><span></span></div>
  <nav class="abs nav">
    <a href="#">HOME</a><a href="#">ABOUT US</a><a href="#">WHAT WE DO</a><a href="#">NEWS BLOG</a><a href="#">ARTICLES</a><a href="#">CLIENTS</a><a href="#">PARTNERS</a><a href="#">CONTACT US</a>
  </nav>
</header>

<section>
  <div class="abs hero" role="img" aria-label="Silhouettes of business people in front of a blue globe and binary code"></div>
  <h1 class="abs hero-title">Serious IT support for business</h1>
  <div class="abs dots"><i></i><i></i><i></i><i></i></div>
  <div class="abs band"></div>
  <div class="abs hero-rule"></div>

  <div class="abs service" style="left:188px"><div class="disc"><svg width="26" height="26" viewBox="0 0 26 26"><path d="M4 22 L15 11" stroke="#fff" stroke-width="4" stroke-linecap="round"/><circle cx="18" cy="8" r="5" fill="none" stroke="#fff" stroke-width="3"/></svg></div>It Support &amp; Management</div>
  <div class="abs service" style="left:319px"><div class="disc"><svg width="30" height="22" viewBox="0 0 30 22"><path d="M7 19 a5 5 0 0 1 0-10 a7 7 0 0 1 13-3 a6 6 0 0 1 3 13 Z" fill="none" stroke="#fff" stroke-width="2.2"/></svg></div>Cloud Computing</div>
  <div class="abs service active" style="left:448px"><div class="disc"><svg width="18" height="28" viewBox="0 0 18 28"><rect x="4" y="10" width="10" height="16" rx="1" fill="none" stroke="#fff" stroke-width="2"/><path d="M9 1 C13 5 14 8 9 9 C4 8 5 5 9 1Z" fill="#fff"/></svg></div>Disaster Recovery</div>
  <div class="abs service" style="left:580px"><div class="disc"><svg width="20" height="28" viewBox="0 0 20 28"><rect x="5" y="2" width="10" height="16" fill="#fff"/><path d="M10 18v5M3 25h14" stroke="#fff" stroke-width="2"/></svg></div>Virtualisation</div>
  <div class="abs service" style="left:703px"><div class="disc"><svg width="28" height="26" viewBox="0 0 28 26"><path d="M14 3 L25 23 M14 3 L3 23 M6 17 H22" stroke="#fff" stroke-width="2.6" fill="none"/></svg></div>CAD Services</div>
</section>

<main>
  <section class="abs about">
    <h2 class="head">ABOUT US</h2>
    <p>Lorem ipsum dolor sit amet, consectetuer adipiscing elit, sed diam nonummy nibh euism od tincidunt ut laoreet dolore magna aliquam erat volutpat. Ut wisi enim ad minim venia m, quis nostrud exerci tation ullamcorper suscipit lobortis nisl ut aliquip ex ea comsed diam nonummy nibh euism od tincidunt ut laoreet dolore magna aliquam erat volutpat.</p>
    <p>Lorem ipsum dolor sit amet, consectetuer adipiscing elit, sed diam nonummy nibh euism od tincidunt ut laoreet dolore magna aliquam erat volutpat. Ut wisi enim ad minim venia m, quis nostrud....</p>
    <a class="readmore">READ MORE...</a>
  </section>
  <div class="abs team">
    <div class="team-photo" role="img" aria-label="Group photo of the team"></div>
    <div class="team-label">OUR TEAM</div>
  </div>

  <section class="abs col" style="left:197px">
    <h2 class="head">TESTIMONIALS</h2>
    <div class="card">
      <div class="testi"><div class="person"><div class="avatar" role="img" aria-label="Portrait of client"></div><b>Paul Harding</b><small>Businessman</small></div>
        <p class="quote">Lorem ipsum dolor sit amet, consectetuer adipiscing elit, sed diam nonummyol nibh euismod tincidunt ut laoreet dolore magnarpl aliquam erat volutpat. Ut wisi enim adm minim. ”</p></div>
      <div class="testi"><div class="person"><div class="avatar" role="img" aria-label="Portrait of client"></div><b>Paul Harding</b><small>Businessman</small></div>
        <p class="quote">Lorem ipsum dolor sit amet, consectetuer adipiscing elit, sed diam nonummyol nibh euismod tincidunt ut laoreet dolore magnarpl aliquam erat volutpat. Ut wisi enim adm minim. ”</p></div>
    </div>
    <div class="pager"><svg width="34" height="14" viewBox="0 0 34 14"><circle cx="7" cy="7" r="6" fill="none" stroke="#555"/><path d="M10 7H4M6 5L4 7L6 9" stroke="#555" fill="none"/><circle cx="27" cy="7" r="6" fill="none" stroke="#555"/><path d="M24 7H30M28 5L30 7L28 9" stroke="#555" fill="none"/></svg></div>
  </section>

  <section class="abs col" style="left:534px">
    <h2 class="head">LATEST NEWS</h2>
    <div class="card">
      <div class="news"><svg width="30" height="30" viewBox="0 0 30 30"><rect x="2" y="5" width="26" height="23" rx="2" fill="none" stroke="#555" stroke-width="2"/><path d="M2 11H28M8 2v6M22 2v6M7 15h4M13 15h4M19 15h4M7 20h4M13 20h4M19 20h4" stroke="#555" stroke-width="2"/></svg><div><time>12-APR-2014</time><p>Lorem ipsum dolor sit amet, consectetuer adipiscil ng elit, sed diam nonummy nibh...</p></div></div>
      <div class="news"><svg width="30" height="30" viewBox="0 0 30 30"><rect x="2" y="5" width="26" height="23" rx="2" fill="none" stroke="#555" stroke-width="2"/><path d="M2 11H28M8 2v6M22 2v6M7 15h4M13 15h4M19 15h4M7 20h4M13 20h4M19 20h4" stroke="#555" stroke-width="2"/></svg><div><time>15-APR-2014</time><p>Lorem ipsum dolor sit amet, consectetuer adipiscil ng elit, sed diam nonummy nibh...</p></div></div>
      <div class="news"><svg width="30" height="30" viewBox="0 0 30 30"><rect x="2" y="5" width="26" height="23" rx="2" fill="none" stroke="#555" stroke-width="2"/><path d="M2 11H28M8 2v6M22 2v6M7 15h4M13 15h4M19 15h4M7 20h4M13 20h4M19 20h4" stroke="#555" stroke-width="2"/></svg><div><time>17-APR-2014</time><p>Lorem ipsum dolor sit amet, consectetuer adipiscil ng elit, sed diam nonummy nibh...</p></div></div>
    </div>
    <div class="pager"><svg width="34" height="14" viewBox="0 0 34 14"><circle cx="7" cy="7" r="6" fill="none" stroke="#555"/><path d="M10 7H4M6 5L4 7L6 9" stroke="#555" fill="none"/><circle cx="27" cy="7" r="6" fill="none" stroke="#555"/><path d="M24 7H30M28 5L30 7L28 9" stroke="#555" fill="none"/></svg></div>
  </section>
</main>

<footer>
  <div class="abs footer"></div>
  <div class="abs foot" style="left:198px;top:1070px">
    <div class="fh">Quick Links</div>
    <div class="links"><span>HOME</span><span>ARTICLES</span><span>ABOUT US</span><span>CLIENTS</span><span>WHAT WE DO</span><span>PARTNERS</span><span>NEWS BLOG</span><span>CONTACT US</span></div>
  </div>
  <div class="abs vr" style="left:388px"></div>
  <div class="abs news-form foot" style="left:430px;top:1071px">
    <div class="fh">Newsletter Signup</div>
    <p>Lorem ipsum dolor sit amet,<br>consectetuer adipiscing elit.</p>
    <div class="email">Enter your email address</div>
    <span class="submit">SUBMIT</span>
  </div>
  <div class="abs vr" style="left:593px"></div>
  <div class="abs fh" style="left:635px;top:1071px">Contact Info</div>
  <div class="abs map" role="img" aria-label="Street map showing office location"></div>
  <div class="abs cinfo">
    <div><svg width="10" height="12" viewBox="0 0 10 12"><path d="M5 12C1 7 1 5 1 4.5a4 4 0 0 1 8 0C9 5 9 7 5 12Z" fill="var(--gold)"/><circle cx="5" cy="4.5" r="1.6" fill="#333"/></svg><span>Lorem ipsum dolor sit<br>amet, consectetuer<br>adipiscing elit.</span></div>
    <div><svg width="10" height="10" viewBox="0 0 10 10"><circle cx="5" cy="5" r="4.3" fill="none" stroke="var(--gold)"/><path d="M3.5 3c0 2 1.5 3.5 3.5 3.5" stroke="var(--gold)" fill="none" stroke-width="1.3"/></svg><span>020 7946 0123</span></div>
    <div><svg width="10" height="8" viewBox="0 0 10 8"><rect width="10" height="8" fill="var(--gold)"/><path d="M0 0L5 4L10 0" stroke="#333" fill="none"/></svg><span>website@plumbcorner.net</span></div>
  </div>
  <div class="abs bottombar">© 2014 plumbcorner. All Rights Reserved.</div>
</footer>
</body>
</html>
```